Health Education Non-Profit Needs a Designer to Layout Magazine (Contest)

Hello, we are looking for someone to layout our print magazine. We'd like to work with someone who also has graphic design experience manipulating photos (see 2 sample issue links below for examples). Ad design is also needed. We like the current design of our magazine, so we are hoping our next designer can maintain the same look and feel as our previous magazines. Samples of our past two issues can be found at https://www.harbolwellness.org/wp-content/uploads/2019/03/issue-09-feb-2019.pdf and https://www.harbolwellness.org/wp-content/uploads/2018/11/the-bright-almanac-2018-05-issue-08.pdf

There are typically 2-4 different issues per year with around 11 articles in each issue. Issues are 24 pages. If there is a lot of white space, we may ask the designer to design an ad at the end of the article. We are looking to work with someone who is responsive and has a quick turnaround time (e.g., takes around 3 weeks to design the entire issue).

For this contest, please design a cover and article. Please refer to our last two issues (links above) before designing. We would like to see how the designer can take the images and edit them in a way that incorporates them seamlessly into the magazine as has been done in the past. Our end goal will be for the designer to design the entire issue and future issues. We anticipate this contest will not cover the entire cost of the work for completing the issue. When we find a designer we like, we will work out details for additional payment. Images can be found here: https://files.quorvanshare.net/folders/7KpTzRwq2LmXvNb4Hs9JdYeCa0FgUi3Q?usp=sharing

```html
<!DOCTYPE html>
<html lang="en">
<head>
<meta charset="utf-8">
<title>Bright Almanac — Cover and Article Spread</title>
<link rel="stylesheet" href="https://fonts.googleapis.com/css2?family=Montserrat:ital,wght@0,400;0,600;0,800;1,700&family=Open+Sans:wght@400;600&display=swap">
<style>
  :root{
    --bg:#ececec;
    --paper:#ffffff;
    --ink:#2b2b2b;
    --muted:#6b6b6b;
    --brand:#1d3f7a;
    --sky:#cfe9f6;
    --sky-deep:#41aee3;
    --blush:#f1c9cb;
    --green:#7cbf3a;
    --red:#d8352a;
    --orange:#f08a1c;
    --teal:#1f8fb8;
    --spice:#b5652c;
  }
  *{box-sizing:border-box;margin:0;padding:0}
  html,body{width:1200px;height:2700px;overflow:hidden}
  body{background:var(--bg);font-family:"Open Sans",Arial,sans-serif;color:var(--ink);position:relative}

  .page{position:absolute;background:var(--paper)}
  .spread{position:absolute;left:50px;width:1100px;height:760px;display:flex}
  .spread .page{position:relative;width:550px;height:760px;overflow:hidden}
  .spread .page.left{border-right:1px solid #d8d8d8}

  /* cover */
  .cover{left:320px;top:105px;width:560px;height:760px;overflow:hidden}
  .masthead{height:110px;background:var(--paper);display:flex;align-items:center;justify-content:center;gap:14px}
  .brand-dot{width:22px;height:22px;border-radius:50%;background:var(--sky-deep)}
  .brand-name{font-family:"Montserrat",Arial,sans-serif;font-weight:800;font-size:42px;color:var(--brand);letter-spacing:-1px}
  .teasers{height:26px;background:var(--sky-deep);display:flex;justify-content:center;gap:26px;align-items:center;font-family:"Montserrat",Arial,sans-serif;font-size:10px;font-weight:600;color:#fff;text-transform:lowercase}
  .teasers span:nth-child(2){color:#ffe066}
  .cover-art{position:absolute;left:0;top:136px;width:560px;height:624px;background:linear-gradient(180deg,var(--sky) 0%,var(--blush) 45%,#e8f5fb 100%)}

  /* article body text */
  .body-text{font-size:9.5px;line-height:1.55;color:var(--ink)}
  .body-text p{margin-bottom:9px;text-align:justify}

  /* spread one */
  .spread-one{top:970px}
  .spread-one .left .body-text{position:absolute;left:40px;top:50px;width:210px}
  .spice-photo{position:absolute;left:0;top:0;width:550px;height:400px;background:linear-gradient(135deg,#3a2a22 0%,#7a3b1c 35%,#c9761f 60%,#4d7a2a 80%,#2b1e18 100%)}
  .mini-brand{position:absolute;right:18px;top:14px;display:flex;align-items:center;gap:6px}
  .mini-brand .brand-dot{width:10px;height:10px}
  .mini-brand .brand-name{font-size:15px;color:#fff;letter-spacing:0}
  .byline{position:absolute;left:330px;top:418px;width:190px;font-size:8px;line-height:1.4;color:var(--muted)}
  .title{position:absolute;left:26px;top:470px;font-family:"Montserrat",Arial,sans-serif;font-weight:800;line-height:.92}
  .title .w1{color:var(--green);font-size:66px;display:block}
  .title .w2{color:var(--green);font-size:30px;font-weight:800}
  .title .w3{color:var(--red);font-size:66px}
  .title .w4{color:var(--orange);font-size:96px;display:block;letter-spacing:-2px}
  .next-arrow{position:absolute;right:22px;bottom:22px}

  /* spread two */
  .spread-two{top:1835px}
  .spread-two .left .cols{position:absolute;left:36px;top:40px;width:478px;display:flex;gap:22px}
  .spread-two .left .cols .body-text{width:228px}
  .plant-photo{position:absolute;left:36px;bottom:36px;width:228px;height:150px;background:linear-gradient(180deg,#dfe7d6 0%,#8fae62 55%,#c8b79a 100%)}
  .recipe{position:absolute;left:24px;top:36px;width:170px;font-size:9.5px;line-height:1.7}
  .recipe h3{font-family:"Montserrat",Arial,sans-serif;font-size:12px;color:var(--spice);margin-bottom:6px}
  .recipe li{list-style:none}
  .powder-photo{position:absolute;right:0;top:0;width:340px;height:400px;background:radial-gradient(circle at 55% 55%,#d08a46 0%,var(--spice) 45%,#5a3520 100%)}
  .callout{position:absolute;left:24px;top:470px;width:500px;font-family:"Montserrat",Arial,sans-serif;font-style:italic;font-weight:700;font-size:30px;line-height:1.15;color:var(--teal)}
  .callout small{display:block;font-size:18px;margin-top:8px}
  .sources{position:absolute;left:24px;bottom:34px;width:500px;font-size:8px;line-height:1.5;color:var(--muted)}
</style>
</head>
<body>

<section class="page cover">
  <header class="masthead">
    <span class="brand-dot"></span>
    <span class="brand-name">Bright Almanac</span>
  </header>
  <div class="teasers">
    <span>inside this issue</span><span>eating out the right way</span><span>tips for travel</span>
  </div>
  <div class="cover-art" role="img" aria-label="Cover illustration: two kidneys being assembled with tweezers, with scattered puzzle pieces"></div>
</section>

<section class="spread spread-one">
  <article class="page left">
    <div class="body-text">
      <p>Latin American cooking draws its depth from a handful of humble seasonings. Cumin, oregano, garlic and dried chiles build warmth without relying on salt, which makes them valuable for anyone watching sodium on a kidney-friendly diet.</p>
      <p>Start with small amounts and taste as you go. Toasting whole seeds in a dry pan for a minute releases their oils and gives a fuller aroma. Fresh herbs such as cilantro and culantro can be added at the end for brightness.</p>
      <p>Citrus is another friend. A squeeze of lime or sour orange lifts beans, rice and grilled fish, and it pairs well with achiote paste for a gentle color and earthy note.</p>
      <p>Ask your dietitian before using salt substitutes, since many contain potassium. Homemade blends let you control every ingredient and keep flavor high.</p>
      <p>Many families keep a jar of sofrito in the kitchen. Made from onion, pepper, garlic and herbs, it can be cooked in batches and frozen in small portions, ready to season soups, stews and rice on busy weeknights without packaged cubes.</p>
      <p>Cooking at home also lets you adjust portions of foods higher in phosphorus, like cheese and dark sodas, while keeping the bold tastes that make a meal feel like home.</p>
    </div>
  </article>
  <article class="page right">
    <div class="spice-photo" role="img" aria-label="Photo of colorful ground spices in wooden spoons on a dark table"></div>
    <div class="mini-brand"><span class="brand-dot"></span><span class="brand-name">Bright Almanac</span></div>
    <p class="byline">By Ana Ruiz RD and Luis Peña MS<br>Renal Nutrition Team</p>
    <h1 class="title"><span class="w1">Cooking</span><span class="w2">with</span><span class="w3">Latin</span><span class="w4">Flavors</span></h1>
    <svg class="next-arrow" width="16" height="18" viewBox="0 0 16 18"><path d="M0 0 L16 9 L0 18 Z" fill="var(--green)"/></svg>
  </article>
</section>

<section class="spread spread-two">
  <article class="page left">
    <div class="cols">
      <div class="body-text">
        <p>Oregano is one of the most common herbs in the region. Mexican oregano has a citrus note, while the Mediterranean kind is sweeter. Both add a clear aroma to bean dishes and grilled chicken without any added salt.</p>
        <p>Cumin brings a warm, smoky taste. Use it with a light hand, because a little goes a long way. Combined with garlic and black pepper, it becomes the base of many adobo blends sold in stores, often with a large amount of salt added.</p>
        <p>Annatto, also called achiote, gives rice and stews a golden color. Its seeds can be steeped in warm oil, then strained, leaving a mild flavored oil that is easy to use in everyday cooking.</p>
        <p>Dried chiles such as ancho and guajillo offer sweetness and gentle heat. Soak them in hot water, blend them into a smooth paste and use it to marinate meats or fish before cooking.</p>
        <p>Culantro has a stronger taste than cilantro and holds up to long cooking. It is a key herb in many Caribbean kitchens.</p>
      </div>
      <div class="body-text">
        <p>Garlic is used almost everywhere. Fresh cloves give the best flavor, but garlic powder is a good choice for dry rubs. Avoid garlic salt, which adds sodium quickly and can raise blood pressure.</p>
        <p>Limes, lemons and sour oranges brighten dishes at the end of cooking. A splash of vinegar works well too, especially in pickled onions that add crunch and tang to tacos, bowls and salads.</p>
        <p>Many store-bought seasonings list salt as the first ingredient. Reading labels helps you choose products with less sodium. Look for blends that say no salt added, and check for potassium chloride, which may not be safe for everyone.</p>
        <p>Making your own mix takes only a few minutes. Combine dried herbs and ground spices in a clean jar, shake well and label it with the date. Most blends keep their flavor for several months when stored away from heat and light.</p>
        <p>Sharing meals is part of the culture. Teaching family members to cook with herbs and spices rather than salt helps everyone at the table eat well and keeps traditions alive for the next generation.</p>
        <p>Bring your favorite recipes to your next visit and ask your care team how to adapt them.</p>
      </div>
    </div>
    <div class="plant-photo" role="img" aria-label="Photo of fresh herb sprigs with roots on a light surface"></div>
  </article>
  <article class="page right">
    <div class="recipe">
      <h3>Homemade Adobo Blend</h3>
      <ul>
        <li>2 tbsp garlic powder</li>
        <li>1 tbsp dried oregano</li>
        <li>1 tbsp ground cumin</li>
        <li>1 tsp black pepper</li>
        <li>1 tsp onion powder</li>
        <li>1 tsp smoked paprika</li>
        <li>½ tsp turmeric</li>
        <li>Mix and store in a jar.</li>
      </ul>
    </div>
    <div class="powder-photo" role="img" aria-label="Photo of ground spice powder in a bowl with a wooden spoon"></div>
    <p class="callout">Tell us, what are your favorite condiments?<small>Send to almanac@harbolreaders.org</small></p>
    <p class="sources">Sources: National nutrition guidelines, 2019. Regional cooking survey, Latin kitchens edition. Sodium and potassium content tables, revised.</p>
  </article>
</section>

</body>
</html>
```